US company marketing to law enforcement needs brochure design

We have created a new logo and now need to update our printed material. What we really need is a "style" or "template" for how our brochures will look in the future. Enclosed is the brochure draft with the old style and logo. Also enclosed is the new logo. As we are marketing to US law enforcement it is important the the brochure design is strong, powerful and that we are looking experienced and trustworthy. However, we also want to look modern in line with the logo update.

Target Market(s)

Law enforcement

Industry/Entity Type

Marketing

```html
<!DOCTYPE html>
<html lang="en">
<head>
<meta charset="utf-8">
<title>Keystone Oversight – Comprehensive Offender Programs Brochure</title>
<link href="https://fonts.googleapis.com/css2?family=Roboto+Condensed:wght@700&family=Marcellus+SC&family=Fira+Sans:wght@400;600&family=Open+Sans:wght@400;600&display=swap" rel="stylesheet">
<style>
  :root{
    --navy:#253f77;
    --navy-deep:#1c3366;
    --blue:#2f84c8;
    --sky:#49a9e6;
    --paper:#f1f2f4;
    --mist:#e4e6ea;
    --bar:#8e9095;
    --ink:#3b3f46;
    --grey-name:#7d8087;
    --white:#ffffff;
    --stage:#e8e6e2;
  }
  *{box-sizing:border-box;margin:0;padding:0}
  html,body{width:922px;height:1200px;overflow:hidden}
  body{background:var(--stage);position:relative;font-family:"Open Sans",sans-serif;color:var(--ink)}
  .spread{position:absolute;left:51px;width:820px;overflow:hidden;box-shadow:0 2px 8px rgba(0,0,0,.18)}
  .spread--outside{top:52px;height:534px}
  .spread--inside{top:610px;height:537px;background:var(--mist)}
  .panel{position:absolute;top:0;height:100%;width:410px;overflow:hidden}
  .panel--back{left:0;background:linear-gradient(#ffffff,#eef0f3)}
  .panel--front{left:410px;background:var(--paper)}

  .brand{position:absolute;display:flex;align-items:center;gap:9px}
  .brand__mark{width:38px;height:38px;border-radius:50%;background:var(--navy)}
  .brand__name{font-family:"Open Sans",sans-serif;font-weight:600;font-size:20px;color:var(--grey-name);letter-spacing:-.2px}
  .panel--back .brand{left:74px;top:34px}
  .panel--front .brand{left:116px;top:234px}

  .photo{position:absolute}
  .photo--handshake{left:0;top:110px;width:410px;height:424px;background:linear-gradient(160deg,#dbe6f0 0%,#ffffff 35%,#c9b7a6 60%,#5b6878 100%)}
  .panel--back .contact{position:absolute;bottom:16px;left:24px;right:28px;display:flex;justify-content:space-between;font-size:10.5px;color:var(--white);letter-spacing:.3px}

  .front-top{position:absolute;left:0;top:0;width:410px;height:280px}
  .front-title{position:absolute;left:34px;top:22px;font-family:"Roboto Condensed",sans-serif;font-weight:700;font-size:20px;color:var(--white)}
  .program-list{position:absolute;left:34px;top:66px;list-style:none;font-family:"Marcellus SC",serif;font-size:15px;line-height:23.5px;color:var(--white);letter-spacing:.5px}
  .photo--courthouse{left:0;top:272px;width:410px;height:262px;background:linear-gradient(90deg,#8a6a2e 0%,#b8924a 22%,#dfe3e8 40%,#f4f5f7 70%,#c7ccd3 100%)}

  .inside-top{position:absolute;left:0;top:0;width:410px;height:171px;background:var(--navy)}
  .inside-title{position:absolute;left:0;width:410px;top:22px;text-align:center;font-family:"Roboto Condensed",sans-serif;font-weight:700;font-size:19px;color:var(--white);letter-spacing:.3px}
  .inside-sub{position:absolute;left:30px;width:350px;top:58px;text-align:center;font-family:"Marcellus SC",serif;font-size:13px;line-height:18px;color:var(--white)}
  .stage-row{position:absolute;top:113px;height:36px;left:0;width:410px}
  .stage{position:absolute;top:2px;height:32px;background:linear-gradient(#3a9ae0,#1569b3);border:1px solid #9cd1f5;color:var(--white);font-size:7.5px;font-weight:600;display:flex;align-items:center;justify-content:center;text-align:center;line-height:9px}
  .stage-icon{position:absolute;top:0;height:36px;border-radius:4px}
  .stage-icon--cuffs{left:8px;width:30px;background:linear-gradient(#6d7075,#2c2e33)}
  .stage-icon--gavel{left:206px;width:50px;background:linear-gradient(#8a5a33,#4d2f19)}
  .stage-icon--badge{left:360px;width:34px;border-radius:50%;background:radial-gradient(#e6c25a,#a27c1c)}

  .flex-block{position:absolute;left:0;top:171px;width:410px;height:162px;background:var(--mist);text-align:center}
  .flex-block__line1{margin-top:24px;font-family:"Fira Sans",sans-serif;font-weight:600;font-size:22px;color:var(--navy)}
  .flex-block__line2{font-family:"Fira Sans",sans-serif;font-size:21px;color:var(--navy);margin-top:2px}
  .flex-block__note{margin:22px auto 0;width:330px;font-size:10px;line-height:14px;letter-spacing:.4px;text-transform:uppercase;color:#2e3137}

  .strip{position:absolute;top:333px;left:0;width:820px;height:32px;background:var(--bar);color:var(--white);font-size:13px;letter-spacing:.6px}
  .strip span{position:absolute;top:7px}
  .strip__phone{left:140px}
  .strip__web{left:530px}

  .photo--meeting{left:432px;top:16px;width:372px;height:148px;background:linear-gradient(100deg,#d9cfc4 0%,#f2ede7 40%,#c0ac98 70%,#7c7a7c 100%)}
  .caption{position:absolute;left:432px;top:164px;width:372px;height:35px;background:linear-gradient(#2b8ad6,#1a5fae);color:var(--white);text-align:center}
  .caption__title{font-family:"Marcellus SC",serif;font-size:14px;line-height:17px;padding-top:2px;letter-spacing:.5px}
  .caption__text{font-size:7.5px}

  .menu{position:absolute;top:210px}
  .menu__heading{font-family:"Marcellus SC",serif;font-size:11.5px;color:var(--navy);line-height:13px;letter-spacing:.3px;white-space:nowrap}
  .menu ul{list-style:none;font-size:6.4px;line-height:9.8px;color:#383b42;white-space:nowrap}
  .menu li{padding-left:9px;position:relative}
  .menu li::before{content:"";position:absolute;left:0;top:2.5px;width:5px;height:5px;background:var(--blue)}
  .menu--conditions{left:432px;width:204px}
  .menu--conditions .cols{display:flex;gap:6px;margin-top:8px}
  .menu--conditions ul:first-child{width:100px}
  .menu--conditions ul:last-child{width:98px}
  .menu--admin{left:642px;width:162px;padding-left:12px;border-left:1px solid #b9bdc4;height:110px}
  .menu--admin ul{margin-top:8px}

  .features{position:absolute;left:0;top:365px;width:820px;height:172px;background:var(--navy);display:flex}
  .feature{flex:1;padding:16px 22px 0 24px;border-right:1px solid #3a5592}
  .feature:last-child{border-right:none}
  .feature h3{font-family:"Marcellus SC",serif;font-weight:400;font-size:12px;line-height:14px;color:var(--white);height:34px;letter-spacing:.3px}
  .feature p{font-size:6.3px;line-height:10.5px;color:#dfe5f2;text-align:justify;margin-top:6px}
  .feature p + p{margin-top:8px}
</style>
</head>
<body>

<section class="spread spread--outside" aria-label="Brochure outside">
  <div class="panel panel--back">
    <div class="brand"><span class="brand__mark"></span><span class="brand__name">KeystoneOversight</span></div>
    <div class="photo photo--handshake" role="img" aria-label="Photo of two business people shaking hands in an office"></div>
    <div class="contact"><span>www.keystoneoversight.org</span><span>1-800-555-0142</span></div>
  </div>

  <div class="panel panel--front">
    <svg class="front-top" viewBox="0 0 410 280" preserveAspectRatio="none" aria-hidden="true">
      <path d="M0 0H410V150C330 150 300 195 220 205C130 216 60 200 0 225Z" fill="#253f77"/>
      <path d="M0 225C60 200 130 216 220 205C300 195 330 150 410 150V162C330 162 305 205 222 214C130 226 60 212 0 236Z" fill="#2f84c8"/>
      <path d="M0 236C60 212 130 226 222 214C305 205 330 162 410 162V166C332 168 306 210 222 219C130 230 60 218 0 240Z" fill="#8d9096"/>
    </svg>
    <h1 class="front-title">Comprehensive Offender Programs</h1>
    <ul class="program-list">
      <li>Pre-Trial</li><li>Diversion</li><li>Deferred Prosecution</li><li>Jail Alternative</li><li>Probation</li>
    </ul>
    <div class="photo photo--courthouse" role="img" aria-label="Photo of a bronze Lady Justice statue before a columned courthouse"></div>
    <div class="brand"><span class="brand__mark"></span><span class="brand__name">KeystoneOversight</span></div>
  </div>
</section>

<section class="spread spread--inside" aria-label="Brochure inside">
  <div class="inside-top">
    <h2 class="inside-title">COMPREHENSIVE OFFENDER SOLUTION</h2>
    <p class="inside-sub">We administer Offender Programs at every stage of the criminal justice process</p>
    <div class="stage-row">
      <div class="stage-icon stage-icon--cuffs" role="img" aria-label="Handcuffs"></div>
      <div class="stage" style="left:66px;width:40px">Pre-Trial</div>
      <div class="stage" style="left:112px;width:38px">Diversion</div>
      <div class="stage" style="left:155px;width:47px">Deferred<br>Prosecution</div>
      <div class="stage-icon stage-icon--gavel" role="img" aria-label="Judge's gavel"></div>
      <div class="stage" style="left:264px;width:46px">Jail<br>Alternative</div>
      <div class="stage" style="left:313px;width:41px">Probation</div>
      <div class="stage-icon stage-icon--badge" role="img" aria-label="Sheriff's star badge"></div>
    </div>
  </div>

  <div class="flex-block">
    <p class="flex-block__line1">flexible solution for</p>
    <p class="flex-block__line2">your jurisdiction’s needs</p>
    <p class="flex-block__note">Not a one size fits all solution:<br>each program developed and administered to your specification</p>
  </div>

  <div class="photo photo--meeting" role="img" aria-label="Photo of a couple meeting with an adviser at a desk"></div>
  <div class="caption">
    <p class="caption__title">CUSTOM SOLUTION</p>
    <p class="caption__text">All offender programs are customized to meet the unique needs of your jurisdiction</p>
  </div>

  <div class="menu menu--conditions">
    <p class="menu__heading">Full menu of Conditions</p>
    <div class="cols">
      <ul>
        <li>Case Management</li><li>Offender Education</li><li>Fine and Fee Recovery</li><li>Inter-active Journaling</li><li>Alcohol monitoring</li><li>Community Resource Referrals</li><li>Curfew monitoring</li><li>Offender Communication</li><li>Reporting</li>
      </ul>
      <ul>
        <li>Face to face meetings</li><li>Group Counselling</li><li>Victim Restitution Recovery</li><li>Drug testing</li><li>Community Service</li><li>GPS monitoring</li><li>House detention</li><li>Preparation of court paperwork</li>
      </ul>
    </div>
  </div>

  <div class="menu menu--admin">
    <p class="menu__heading">Comprehensive<br>Administrative Services</p>
    <ul>
      <li>Eligible case screening</li><li>Case referral</li><li>Data entry</li><li>Electronic case files</li><li>Offender communication</li><li>Reporting</li>
    </ul>
  </div>

  <div class="strip"><span class="strip__phone">1-800-555-0142</span><span class="strip__web">www.keystoneoversight.org</span></div>

  <div class="features">
    <article class="feature">
      <h3>Experienced<br>Professionals</h3>
      <p>Our case management and operations team brings decades of experience building and running programs for prosecutors, courts and probation offices. Every program is shaped around the goals of each jurisdiction.</p>
    </article>
    <article class="feature">
      <h3>Control /<br>Transparency</h3>
      <p>Your office sets the parameters and offender requirements for every program and keeps full control to adjust them at any time.</p>
      <p>You and your designated staff receive round-the-clock online access to all case files, with a record of every action taken.</p>
    </article>
    <article class="feature">
      <h3>Save Resources /<br>Reduce case loads</h3>
      <p>We supply the resources to reduce your staff's workload and reach a quick resolution for each case. Our team handles all program administration, referrals, reporting and resolution.</p>
    </article>
    <article class="feature">
      <h3>Technology /<br>Equipment</h3>
      <p>Our technology automates processes so staff can focus on direct interaction with each offender.</p>
      <p>Where electronic monitoring is needed, we use only current, proven equipment to ensure offender accountability and public safety.</p>
    </article>
  </div>
</section>

</body>
</html>
```